Academy of Hops Business Card/Stamp card
Business card and stamp card
Creative Brief
Use specific fonts
Any font is fine.
Modern
Academy of Hops
2374 Larkwood Avenue Suite 410 Sacramento, CA 95816
NOmail@NOmailbox.example
www.TheZqm.example
The Largest Selection Of Craft Beers On Tap In All Of Sacramento! 100 on Tap
It will be a stamp card. Must contain all of this.... Collect 10 Stamps, and get one Zqm Bar Bite FREE Card must be stamped at the time of purchase. Stamps can be combined. Card(s) must be surrendered to receive a free Bar Bite. Not valid for employees and their relatives. Some restrictions may apply. Cannot be combined with any other offers. Not valid without coupon, or if reproduced. This offer can be canceled at anytime without notice.

```html
<!DOCTYPE html>
<html lang="en">
<head>
<meta charset="utf-8">
<title>Academy of Hops – Business Card and Stamp Card</title>
<link rel="stylesheet" href="https://fonts.googleapis.com/css2?family=Open+Sans:wght@400;600;700;800&display=swap">
<style>
  :root {
    --bg: #e9e7e3;
    --card: #ffffff;
    --blue: #2e64a3;
    --gold: #d4a43a;
    --ink: #4a4a4a;
    --muted: #777777;
    --rule: #c9c9c9;
  }
  html, body {
    margin: 0;
    padding: 0;
    width: 1200px;
    height: 901px;
    overflow: hidden;
    background: var(--bg);
    font-family: "Open Sans", Arial, sans-serif;
  }
  .canvas { position: relative; width: 1200px; height: 901px; }
  .card {
    position: absolute;
    width: 600px;
    height: 340px;
    background: var(--card);
    box-shadow: 0 6px 18px rgba(0,0,0,.18);
    overflow: hidden;
  }
  .card--stamp { left: 150px; top: 80px; }
  .card--back  { left: 450px; top: 480px; }

  .brand { display: flex; align-items: center; gap: 8px; }
  .brand__dot { width: 18px; height: 18px; border-radius: 50%; background: var(--gold); flex: none; }
  .brand__name { font-weight: 800; color: var(--blue); letter-spacing: 1px; line-height: 1; }

  /* Stamp card */
  .stamp-header {
    position: absolute;
    left: 26px; right: 26px; top: 20px;
    display: flex; align-items: center; gap: 16px;
    padding-bottom: 12px;
    border-bottom: 1px solid var(--rule);
  }
  .stamp-header .brand__name { font-size: 36px; }
  .stamp-header__text { border-left: 1px solid var(--rule); padding-left: 16px; }
  .venue-name { margin: 0; font-size: 17px; font-weight: 700; color: var(--blue); }
  .tagline { margin: 2px 0 0; font-size: 10.5px; color: var(--ink); line-height: 1.35; }
  .tagline strong { color: var(--gold); }

  .offer {
    position: absolute;
    left: 26px; right: 26px; top: 90px;
    margin: 0;
    text-align: center;
    font-size: 14px; font-weight: 600; color: var(--ink);
  }
  .offer strong { color: var(--blue); }

  .stamp-grid {
    position: absolute;
    left: 50%; top: 120px;
    transform: translateX(-50%);
    display: grid;
    grid-template-columns: repeat(5, 40px);
    gap: 10px 16px;
    margin: 0; padding: 0; list-style: none;
  }
  .stamp-grid li {
    width: 40px; height: 40px;
    box-sizing: border-box;
    border: 2px dashed var(--gold);
    border-radius: 50%;
    display: flex; align-items: center; justify-content: center;
    font-size: 12px; font-weight: 600; color: var(--gold);
  }

  .terms {
    position: absolute;
    left: 26px; right: 26px; top: 222px;
    margin: 0;
    font-size: 9px; line-height: 1.45; color: var(--muted);
    text-align: center;
  }
  .stamp-footer {
    position: absolute; left: 0; right: 0; bottom: 0; height: 14px;
    background: var(--blue);
    border-top: 4px solid var(--gold);
  }

  /* Back of business card */
  .card--back .brand { position: absolute; left: 70px; top: 72px; }
  .card--back .brand__dot { width: 22px; height: 22px; }
  .card--back .brand__name { font-size: 48px; }

  .divider {
    position: absolute;
    left: 318px; top: 36px;
    width: 1px; height: 150px;
    background: var(--rule);
  }
  .contact {
    position: absolute;
    left: 332px; top: 36px;
    margin: 0; padding: 0;
    list-style: none;
    font-size: 13px;
    color: var(--ink);
    line-height: 1.35;
  }
  .contact li { display: flex; align-items: center; gap: 7px; margin-bottom: 5px; }
  .contact svg { width: 13px; height: 13px; flex: none; fill: var(--ink); }
  .contact .contact__address { display: block; margin-bottom: 8px; }

  .wave { position: absolute; left: 0; top: 0; width: 600px; height: 340px; }
  .holder {
    position: absolute;
    left: 40px; bottom: 26px; margin: 0;
    color: #fff;
    font-size: 14px;
    letter-spacing: 1.5px;
  }
  .holder__name { font-weight: 600; }
</style>
</head>
<body>
<main class="canvas">
  <section class="card card--stamp" aria-label="Stamp card">
    <header class="stamp-header">
      <div class="brand">
        <span class="brand__dot"></span>
        <span class="brand__name">Zqm</span>
      </div>
      <div class="stamp-header__text">
        <h1 class="venue-name">Academy of Hops</h1>
        <p class="tagline">The Largest Selection Of Craft Beers On Tap In All Of Sacramento! <strong>100 on Tap</strong></p>
      </div>
    </header>

    <p class="offer">Collect 10 Stamps, and get one <strong>Zqm Bar Bite FREE</strong></p>

    <ol class="stamp-grid">
      <li>1</li><li>2</li><li>3</li><li>4</li><li>5</li>
      <li>6</li><li>7</li><li>8</li><li>9</li><li>10</li>
    </ol>

    <p class="terms">Card must be stamped at the time of purchase. Stamps can be combined. Card(s) must be surrendered to receive a free Bar Bite. Not valid for employees and their relatives. Some restrictions may apply. Cannot be combined with any other offers. Not valid without coupon, or if reproduced. This offer can be canceled at anytime without notice.</p>

    <div class="stamp-footer"></div>
  </section>

  <section class="card card--back" aria-label="Business card back">
    <svg class="wave" viewBox="0 0 600 340" aria-hidden="true">
      <path d="M0,262 C180,300 390,220 600,150 L600,340 L0,340 Z" fill="var(--blue)"/>
      <path d="M0,250 C190,292 390,206 600,136" fill="none" stroke="var(--gold)" stroke-width="5"/>
      <path d="M0,236 C200,280 400,196 600,124" fill="none" stroke="#d9d9d9" stroke-width="1.5"/>
    </svg>

    <div class="brand">
      <span class="brand__dot"></span>
      <span class="brand__name">Zqm</span>
    </div>

    <div class="divider"></div>

    <ul class="contact">
      <li class="contact__address">2374 Larkwood Avenue<br>Suite 410<br>Sacramento, CA 95816</li>
      <li>
        <svg viewBox="0 0 16 16"><path d="M3.5 1l2.5 3-1.5 2a9 9 0 0 0 5 5l2-1.5 3 2.5-1.5 2.5C7 14 2 9 1 2.5z"/></svg>
        012 555 0147
      </li>
      <li>
        <svg viewBox="0 0 16 16"><path d="M1 3h14v10H1z M1 3l7 5 7-5" fill="none" stroke="#4a4a4a" stroke-width="1.5"/></svg>
        NOmail@NOmailbox.example
      </li>
      <li>
        <svg viewBox="0 0 16 16"><circle cx="8" cy="8" r="7"/></svg>
        www.TheZqm.example
      </li>
    </ul>

    <p class="holder"><span class="holder__name">MARTA QUILLEN</span> Managing Director</p>
  </section>
</main>
</body>
</html>
```